Brochure for concert

I need a brochure design for the concert. Attached please find last year's brochure (Velmo Concert Programme.pdf).
The contents of this year's brochure can be found in the document 'Concert program.docx.'
The design of the brochure should be consistent with the invitation card.

```html
<!DOCTYPE html>
<html lang="en">
<head>
<meta charset="utf-8">
<title>Band Meadowlark featuring Velmo — Concert Programme</title>
<link rel="stylesheet" href="https://fonts.googleapis.com/css2?family=Cinzel:wght@400;700&family=Great+Vibes&family=Montserrat:wght@400;600&family=Lato:wght@400;700&display=swap">
<style>
:root{
  --backdrop:#d3d3d3;
  --navy:#0d1f3d;
  --navy-deep:#081428;
  --navy-soft:#16305a;
  --gold:#d9a955;
  --gold-light:#f0cf8a;
  --ink:#e9e4d6;
  --emerald:#2f8f3e;
}
*{box-sizing:border-box;margin:0;padding:0}
html,body{width:1200px;height:4800px;overflow:hidden;background:var(--backdrop)}
body{position:relative;font-family:"Lato",sans-serif;color:var(--ink)}
.page{position:absolute;width:464px;height:602px;overflow:hidden;
  background:radial-gradient(ellipse at 50% 40%,var(--navy-soft) 0%,var(--navy) 55%,var(--navy-deep) 100%);
  display:flex;flex-direction:column;align-items:center;padding:70px 52px 60px;text-align:center}
.col-left{left:97px}.col-right{left:628px}
.corner{position:absolute;width:96px;height:110px;opacity:.55}
.corner.tl{top:0;left:0;background:radial-gradient(circle at 0 0,var(--gold) 0%,rgba(217,169,85,.25) 45%,transparent 70%)}
.corner.tr{top:0;right:0;background:radial-gradient(circle at 100% 0,var(--gold) 0%,rgba(217,169,85,.25) 45%,transparent 70%)}
.corner.bl{bottom:0;left:0;width:60px;height:80px;background:radial-gradient(circle at 0 100%,var(--gold) 0%,rgba(217,169,85,.2) 45%,transparent 70%)}
.corner.br{bottom:0;right:0;width:60px;height:80px;background:radial-gradient(circle at 100% 100%,var(--gold) 0%,rgba(217,169,85,.2) 45%,transparent 70%)}
.song-title{font-family:"Cinzel",serif;color:var(--gold);font-size:17px;letter-spacing:1.5px;margin:24px 0 12px;
  border-bottom:1px solid rgba(217,169,85,.6);padding:0 24px 4px}
.intro{font-size:7.5px;line-height:1.45;color:var(--ink);max-width:350px;margin-bottom:18px}
.lyric-box{border:1px solid rgba(217,169,85,.55);border-radius:14px;width:290px;flex:1;max-height:340px;
  padding:22px 18px;display:flex;flex-direction:column;justify-content:center;gap:10px;font-size:7px;line-height:1.5}
.lyric-box p{margin:0}
.continue{font-family:"Cinzel",serif;color:var(--gold);font-size:11px;margin-top:10px}
/* cover */
.cover{padding:0;display:block}
.cover .band{position:absolute;left:0;top:62px;width:464px;text-align:center;white-space:nowrap;
  font-family:"Cinzel",serif;font-weight:700;color:var(--gold);font-size:30px;line-height:1;letter-spacing:1px}
.cover .featuring{position:absolute;left:0;top:104px;width:464px;text-align:center;
  font-family:"Cinzel",serif;color:var(--gold-light);font-size:12px;letter-spacing:4px;line-height:1}
.cover .photo{position:absolute;left:215px;top:140px;width:249px;height:380px;
  background:linear-gradient(160deg,#eae7e0 0%,#3b2a22 45%,#1f6a54 75%,#0c1a33 100%)}
.cover .star{position:absolute;top:128px;left:110px;width:240px;text-align:center;z-index:2;
  font-family:"Great Vibes",cursive;color:var(--gold-light);font-size:64px;line-height:1}
.cover .details{position:absolute;left:6px;top:282px;width:200px;font-family:"Montserrat",sans-serif;font-size:12px;line-height:1.55;color:var(--ink);letter-spacing:1px;text-align:center}
.cover .details sup{font-size:7px}
.cover .stream{position:absolute;left:42px;top:432px;font-family:"Montserrat",sans-serif;font-size:7px;color:var(--ink);z-index:2}
.cover .wordmark{position:absolute;left:92px;top:484px;width:270px;height:38px;border:1px solid var(--gold);z-index:2;
  background:var(--navy-deep);display:flex;align-items:center;justify-content:center;font-family:"Cinzel",serif;color:var(--gold);font-size:20px;white-space:nowrap}
.cover .medallion{position:absolute;left:132px;bottom:-60px;width:200px;height:120px;border-radius:50%;
  background:radial-gradient(circle,rgba(217,169,85,.55),transparent 70%)}
/* program */
.program{padding-top:52px}
.program .heading{font-family:"Cinzel",serif;color:var(--gold);font-size:18px;margin:12px 0 18px;border-bottom:1px solid var(--gold);padding:0 20px 3px}
.program .section{font-family:"Cinzel",serif;color:var(--gold);font-size:13px;margin:6px 0 12px;border-top:1px solid rgba(217,169,85,.6);border-bottom:1px solid rgba(217,169,85,.6);padding:2px 16px}
.program ul{list-style:none;display:grid;grid-template-columns:1fr 1fr;gap:8px 30px;width:280px;margin-bottom:22px;font-family:"Montserrat",sans-serif;font-size:8px;font-weight:600;text-align:left}
.program li::before{content:"";display:inline-block;width:5px;height:5px;border:1px solid var(--gold);border-radius:50%;margin-right:8px;vertical-align:middle}
.program li.center{grid-column:1/3;justify-self:center}
.camper{width:230px;height:90px;margin-top:18px;background:linear-gradient(180deg,transparent,rgba(217,169,85,.25));border-bottom:1px solid var(--gold)}
</style>
</head>
<body>

<section class="page cover col-left" style="top:130px">
  <div class="corner tl"></div><div class="corner tr"></div>
  <h1 class="band">BAND MEADOWLARK</h1>
  <div class="featuring">FEATURING</div>
  <div class="photo" role="img" aria-label="Photo of the young pianist seated at a grand piano"></div>
  <div class="star">Velmo</div>
  <div class="details">JOIN US<br>SATURDAY, AUGUST 21<sup>ST</sup><br>7PM - 8PM<br>48 ALDER COURT<br>FERNBROOK, NJ 08100</div>
  <div class="stream">Stream Link: meet.stagecast.example/4821</div>
  <div class="wordmark">Band Meadowlark</div>
  <div class="medallion" role="img" aria-label="Gold mandala ornament"></div>
</section>

<section class="page program col-right" style="top:130px">
  <div class="corner tl"></div><div class="corner tr"></div><div class="corner bl"></div><div class="corner br"></div>
  <h2 class="heading">PROGRAM</h2>
  <h3 class="section">CLASSICAL</h3>
  <ul><li>Minuet in F Major</li><li>Moonlight Sonata</li><li class="center">Climb Ev'ry Mountain</li></ul>
  <h3 class="section">BROADWAY</h3>
  <ul><li>Jingle Bells</li><li>Castle On A Cloud</li><li>My Favorite Things</li><li>Over the Rainbow</li></ul>
  <h3 class="section">ROCK</h3>
  <ul><li>Sacrifice</li><li>Your Song</li><li>Piano Man</li><li>My Way</li></ul>
  <h3 class="section">VELMO'S OWN COMPOSITIONS</h3>
  <ul><li>Pony's in Denver</li><li>Sunshine Up High</li><li>Gems and Jewels</li><li>Feel the Light</li></ul>
</section>

<section class="page col-left" style="top:786px">
  <div class="corner tl"></div><div class="corner tr"></div><div class="corner bl"></div><div class="corner br"></div>
  <h2 class="song-title">MENUET IN F MAJOR</h2>
  <p class="intro">One of the earliest keyboard pieces by a celebrated classical composer, written in childhood and later collected by the family. Its gentle dance form made it a favourite for young players and an ideal opening for tonight's programme.<br><br>Written for the keyboard, it pairs a graceful melody in the upper voice with a steady, simple line in the left hand.</p>
  <h2 class="song-title">MOONLIGHT SONATA</h2>
  <p class="intro">A much-loved piano sonata whose quiet, flowing opening movement has become one of the most recognised pieces in the repertoire. It was finished in the early nineteenth century and dedicated to a student of the composer. A later critic compared the first movement to moonlight shimmering on a lake, and the name stayed with it ever since.<br><br>The sonata moves from a hushed, dreamlike beginning through a light middle movement to a stormy, brilliant finale. Its daring structure surprised listeners of the time, and it remains a landmark for pianists young and old.</p>
</section>

<section class="page col-right" style="top:786px">
  <div class="corner tl"></div><div class="corner tr"></div><div class="corner bl"></div><div class="corner br"></div>
  <h2 class="song-title">CLIMB EV'RY MOUNTAIN</h2>
  <p class="intro">A stage-musical song of hope, sung as gentle encouragement to keep searching for one's own path through every challenge.</p>
  <div class="lyric-box"><p>Look to every hillside,<br>Walk on through the rain,<br>Follow every river,<br>Till you're home again.</p><p>Look to every hillside,<br>Cross each open plain,<br>Follow every rainbow,<br>Till you find your way.</p><p>A hope that will hold you,<br>All the love you give,<br>Every day of your life<br>For as long as you live.</p></div>
</section>

<section class="page col-left" style="top:1444px">
  <div class="corner tl"></div><div class="corner tr"></div><div class="corner bl"></div><div class="corner br"></div>
  <h2 class="song-title">JINGLE BELLS</h2>
  <p class="intro">One of the best-known seasonal songs in the world, first written for a holiday gathering and later tied forever to winter and festive cheer.</p>
  <div class="lyric-box"><p>Gliding through the snow<br>In a sleigh drawn by one horse<br>Over fields we go<br>Laughing all the way.</p><p>Bells ring bright and clear<br>Hearts are light and gay<br>What fun it is to ride and sing<br>A sleighing song today.</p><p>Jingle bells, jingle bells,<br>Jingle all the way,<br>Oh what fun it is to ride<br>In a one-horse open sleigh.</p><p>Sung again in French,<br>Bells across the snow,<br>Joy to young and old,<br>Wherever we may go.</p></div>
</section>

<section class="page col-right" style="top:1444px">
  <div class="corner tl"></div><div class="corner tr"></div><div class="corner bl"></div><div class="corner br"></div>
  <h2 class="song-title">CASTLE ON A CLOUD</h2>
  <p class="intro">A tender song from a long-running stage musical, sung by a young girl who dreams of a place where she is safe, cared for and free from hard chores.</p>
  <div class="lyric-box"><p>There's a castle high above,<br>Where I go to rest my head,<br>There is nobody there to scold,<br>No one tells me off to bed.</p><p>There's a room that's full of light,<br>Toys and flowers everywhere,<br>Nobody shouts or calls my name,<br>Not in my castle there.</p><p>There's a lady all in white,<br>Sings me softly off to sleep,<br>She is kind and warm and near,<br>Says my dreams are mine to keep.</p></div>
</section>

<section class="page col-left" style="top:2100px">
  <div class="corner tl"></div><div class="corner tr"></div><div class="corner bl"></div><div class="corner br"></div>
  <h2 class="song-title">MY FAVORITE THINGS</h2>
  <p class="intro">A cheerful song from a classic stage and screen musical, listing the small delights that chase away worries on a gloomy day.</p>
  <div class="lyric-box"><p>Raindrops and daisies and warm woolly mittens,<br>Bright paper parcels and sleepy grey kittens,<br>Kites in the sky tied up with strings,<br>These are a few of my favourite things.</p><p>Candles and cocoa and snow on the windows,<br>Sleigh bells and songbirds and bright yellow meadows,<br>Silver-white winters that melt into spring,<br>These are a few of my favourite things.</p><p>When the storm comes,<br>When the skies frown,<br>I simply remember my favourite things<br>And then I don't feel so down.</p></div>
</section>

<section class="page col-right" style="top:2100px">
  <div class="corner tl"></div><div class="corner tr"></div><div class="corner bl"></div><div class="corner br"></div>
  <h2 class="song-title">OVER THE RAINBOW</h2>
  <p class="intro">A beloved ballad from a classic film musical, sung by a young girl who longs for a brighter world beyond the storms of home.</p>
  <div class="lyric-box"><p>When all the world is grey and still,<br>And the rain won't stop its call,<br>Somewhere the sky is clear and blue,<br>Just a step beyond the wall.</p><p>Somewhere over the rainbow, way up high,<br>There's a land I dreamed of once in a lullaby.<br>Somewhere the skies are open and bright,<br>And the dreams you dare to dream take flight.</p><p>Someday I'll wish upon a star<br>And wake where clouds are far behind me,<br>Where worries melt like lemon drops,<br>That's where you'll find me.</p></div>
</section>

<section class="page col-left" style="top:2757px">
  <div class="corner tl"></div><div class="corner tr"></div><div class="corner bl"></div><div class="corner br"></div>
  <h2 class="song-title">SACRIFICE</h2>
  <p class="intro">A heartfelt ballad by a famous singer-pianist and his longtime lyricist, about the quiet give-and-take that holds two people together. It became one of his best-loved hits.</p>
  <div class="lyric-box"><p>It's a quiet kind of day<br>When the hours drift slowly by,<br>And every word we never say<br>Is waiting in the sky.</p><p>Cold, cold heart, hard done by you,<br>Some things look better, baby,<br>Just passing through.</p><p>And it's no sacrifice, just a simple word,<br>Two hearts that learn to listen<br>To what they've heard.</p><p>And it's no sacrifice,<br>No sacrifice at all.</p></div>
</section>

<section class="page col-right" style="top:2757px">
  <div class="corner tl"></div><div class="corner tr"></div><div class="corner bl"></div><div class="corner br"></div>
  <h2 class="song-title">YOUR SONG</h2>
  <p class="intro">An early hit by a famous singer-songwriter duo, this gentle love song is often ranked among the greatest songs of its era.</p>
  <div class="lyric-box"><p>It's a little bit strange, this feeling inside,<br>I'm not the kind who can easily hide,<br>I don't have much money, but if I did,<br>I'd buy us a house where we both could live.</p><p>If I were a painter, but then again no,<br>Or a maker of magic in a travelling show,<br>I know it's not much, but it's the best I can do,<br>My gift is my song, and this one's for you.</p><p>And you can tell everybody this is your song,<br>It may be quite simple, but now that it's done,<br>I hope you don't mind that I put down in words<br>How wonderful life is while you're in the world.</p></div>
</section>

<section class="page col-left" style="top:3413px">
  <div class="corner tl"></div><div class="corner tr"></div><div class="corner bl"></div><div class="corner br"></div>
  <h2 class="song-title">PIANO MAN</h2>
  <p class="intro">A signature song by a celebrated American singer-songwriter, drawn from his time playing piano in a small lounge and the regulars he met there each night.</p>
  <div class="lyric-box"><p>It's nine o'clock on a Saturday,<br>The regular crowd files in,<br>There's an old man sitting next to me,<br>Humming a tune on his gin.</p><p>He says, son, can you play me a memory,<br>I'm not really sure how it goes,<br>But it's sad and it's sweet and I knew it complete<br>When I wore a younger man's clothes.</p><p>La la la, de de da,<br>La la, de de da da dum.</p><p>Sing us a song, you're the piano man,<br>Sing us a song tonight,<br>Well, we're all in the mood for a melody<br>And you've got us feeling all right.</p></div>
  <div class="continue">CONTINUE</div>
</section>

<section class="page col-right" style="top:3413px">
  <div class="corner tl"></div><div class="corner tr"></div><div class="corner bl"></div><div class="corner br"></div>
  <h2 class="song-title">PIANO MAN</h2>
  <p class="intro">The song continues through the night, sketching the waiters, dreamers and friends who gather around the piano to forget their troubles for a while.</p>
  <div class="lyric-box"><p>Now Paul is a writer who never finished,<br>He never had time for a wife,<br>And he talks with Davy, still in the navy,<br>And probably will be for life.</p><p>And the waitress is practising politics,<br>As the businessmen slowly get stoned,<br>Yes, they're sharing a drink they call loneliness,<br>But it's better than drinking alone.</p><p>Sing us a song, you're the piano man,<br>Sing us a song tonight,<br>Well, we're all in the mood for a melody<br>And you've got us feeling all right.</p></div>
</section>

<section class="page col-left" style="top:4069px">
  <div class="corner tl"></div><div class="corner tr"></div><div class="corner bl"></div><div class="corner br"></div>
  <h2 class="song-title">PONIES IN DENVER</h2>
  <p class="intro">This is my own composition, written during a family trip west, where I met the ponies that gave the song its name.</p>
  <div class="lyric-box" style="max-height:130px;flex:none;height:130px"><p>I couldn't find the pony that I wanted,<br>So I waited by the gate,<br>Then the brown one trotted over,<br>And I knew it was worth the wait.</p><p>So I rode across the mountain,<br>Under skies so wide and free.</p></div>
  <h2 class="song-title">SUNSHINE UP HIGH</h2>
  <p class="intro">This is my first composition, written at our home one bright spring morning.</p>
  <div class="lyric-box" style="max-height:110px;flex:none;height:110px"><p>Sunshine up high, on mountain treetops,<br>Down below rivers flow,<br>Birds and flowers wake,<br>And I sing along.</p></div>
</section>

<section class="page col-right" style="top:4069px">
  <div class="corner tl"></div><div class="corner tr"></div><div class="corner bl"></div><div class="corner br"></div>
  <h2 class="song-title">GEMS AND JEWELS</h2>
  <p class="intro">I wrote this song while on a road trip with my parents during the winter holidays.</p>
  <div class="lyric-box" style="max-height:150px;flex:none;height:150px;border:none"><p>Come along to see what's written in my tale,<br>Sing with me, it's what's written in my heart,<br>See how bright the gems and jewels shine,<br>But of all the riches I have found,<br>Family is the best treasure of mine.</p></div>
  <div class="camper" role="img" aria-label="Line drawing of a camper van beneath mountains and pine trees"></div>
</section>

</body>
</html>
```